Vorsen Kinetics Iron Tide Multi Vitamin Label Design

We need a label design for our Sports Performance Daily Multi Vitamin specially created and branded for our Vorsen Kinetics line for the Halbrook State University. The feel is edgy, sports nutrition. Two logos need to be incorporated... Vorsen and the Collective Logo attached. The colors should be the official colors of the Halbrook State University. The font may also be the Georgia font... or the Vorsen font. Or any font. A hydration product will also be created later on...so this label design may be used on many products. Please utilize the collective logo similar to the use in the attached photo. No official trademark items from the Halbrook State University should be used. Attached is also an image if the bottle (white) that will be used for the vitamin. Please use red, black, grey, white. We are looking for the front design only right now and once selected, will work on the nutrition/back label portion with the artist.

```html
<!DOCTYPE html>
<html lang="en">
<head>
<meta charset="utf-8">
<title>Vorsen Kinetics Iron Tide Multi Vitamin – Label Fronts</title>
<link rel="stylesheet" href="https://fonts.googleapis.com/css2?family=Permanent+Marker&family=Oswald:wght@500;700&family=Russo+One&family=Michroma&display=swap">
<style>
  :root {
    --red: #e4232b;
    --red-deep: #8e1116;
    --black: #0b0b0c;
    --grey: #a7a8ab;
    --grey-dark: #5a5b5e;
    --white: #ffffff;
    --stage: #eeeeef;
  }
  * { margin: 0; padding: 0; box-sizing: border-box; }
  html, body { width: 1200px; height: 2265px; overflow: hidden; }
  body { background: var(--stage); position: relative; font-family: "Oswald", sans-serif; }

  .label {
    position: absolute; left: 160px; width: 880px; height: 1058px;
    background: var(--black); overflow: hidden; color: var(--white);
  }
  .label--red { top: 50px; }
  .label--grey { top: 1158px; }

  .brush-band { position: absolute; left: 0; right: 0; bottom: 0; height: 400px; }
  .label--red .brush-band {
    background: linear-gradient(170deg, rgba(228,35,43,0) 0%, var(--red-deep) 30%, var(--red) 70%, #c81a21 100%);
  }
  .label--grey .brush-band {
    background: linear-gradient(170deg, rgba(167,168,171,0) 0%, var(--grey-dark) 30%, var(--grey) 70%, #8d8e91 100%);
  }

  .brand-name {
    position: absolute; left: 0; right: 0; text-align: center;
    font-family: "Oswald", sans-serif; font-weight: 700; letter-spacing: 4px;
    text-transform: uppercase;
  }
  .label--red .brand-name { top: 50px; font-size: 96px; color: #d9d9db; }
  .label--grey .brand-name { top: 50px; font-size: 96px; color: var(--red); }

  .product-line {
    position: absolute; left: 0; right: 0; text-align: center;
    font-family: "Oswald", sans-serif; font-weight: 500; text-transform: uppercase;
  }
  .label--red .product-line { top: 218px; font-size: 30px; letter-spacing: 10px; }
  .label--grey .product-line { top: 268px; font-size: 40px; letter-spacing: 14px; }

  .label--red .title {
    position: absolute; left: 80px; right: 0; top: 260px; text-align: center;
    font-family: "Permanent Marker", cursive; font-size: 250px; line-height: 1;
    color: #e9e9ea; transform: rotate(-5deg);
  }
  .label--red .subtitle {
    position: absolute; left: 120px; right: 0; top: 540px; text-align: center;
    font-family: "Permanent Marker", cursive; font-size: 84px; color: var(--white);
    transform: rotate(-4deg);
  }
  .label--grey .title {
    position: absolute; left: 0; right: 0; top: 325px; text-align: center;
    font-family: "Russo One", sans-serif; font-size: 200px; line-height: 1;
    font-style: italic; color: transparent; -webkit-text-stroke: 4px var(--red);
    letter-spacing: 4px; transform: rotate(-3deg);
  }
  .label--grey .subtitle {
    position: absolute; left: 0; right: 0; top: 520px; text-align: center;
    font-family: "Michroma", sans-serif; font-size: 44px; letter-spacing: 30px;
    color: var(--white); transform: rotate(-3deg);
  }

  .seal {
    position: absolute; left: 650px; top: 645px; width: 220px; height: 220px;
    border-radius: 50%; background: var(--white); border: 10px solid #d5d5d7;
  }
  .label--grey .seal { top: 650px; }

  .stats { position: absolute; left: 55px; bottom: 60px; display: flex; align-items: flex-end; }
  .stat { padding: 0 18px; border-right: 3px solid rgba(255,255,255,.85); color: var(--white); text-transform: uppercase; }
  .stat:first-child { padding-left: 0; }
  .stat__value { display: block; font-size: 60px; font-weight: 500; line-height: 1; }
  .stat__value small { font-size: 30px; }
  .stat__label { display: block; font-size: 22px; line-height: 1; margin-top: 4px; }
  .stat--free .stat__label { font-size: 22px; margin: 0 0 4px; }
  .stat--free .stat__value { font-size: 42px; }
  .label--grey .stat { color: #1a1a1b; border-color: rgba(20,20,20,.85); }

  .count { position: absolute; right: 160px; bottom: 55px; text-align: center; text-transform: uppercase; }
  .count__value { display: block; font-size: 84px; font-weight: 700; line-height: 1; color: var(--white); }
  .count__label { display: block; font-size: 24px; color: var(--white); }
  .label--grey .count__value, .label--grey .count__label { color: #1a1a1b; }
</style>
</head>
<body>

<section class="label label--red" aria-label="Red label front">
  <div class="brush-band" role="img" aria-label="Red brush-stroke texture sweeping up from the bottom of the label"></div>
  <div class="brand-name">Vorsen</div>
  <div class="product-line">Multi Vitamin</div>
  <div class="title">Sports</div>
  <div class="subtitle">Performance</div>
  <div class="seal" role="img" aria-label="Collective seal"></div>
  <div class="stats">
    <div class="stat"><span class="stat__value">25<small>G</small></span><span class="stat__label">Protein</span></div>
    <div class="stat"><span class="stat__value">5</span><span class="stat__label">Protein<br>Sources</span></div>
    <div class="stat stat--free"><span class="stat__label">Gluten</span><span class="stat__value">Free</span></div>
  </div>
  <div class="count"><span class="count__value">50</span><span class="count__label">Capsules</span></div>
</section>

<section class="label label--grey" aria-label="Grey label front">
  <div class="brush-band" role="img" aria-label="Grey brush-stroke texture sweeping up from the bottom of the label"></div>
  <div class="brand-name">Vorsen</div>
  <div class="product-line">Multi Vitamin</div>
  <div class="title">Sports</div>
  <div class="subtitle">Performance</div>
  <div class="seal" role="img" aria-label="Collective seal"></div>
  <div class="stats">
    <div class="stat"><span class="stat__value">25<small>G</small></span><span class="stat__label">Protein</span></div>
    <div class="stat"><span class="stat__value">5</span><span class="stat__label">Protein<br>Sources</span></div>
    <div class="stat stat--free"><span class="stat__label">Gluten</span><span class="stat__value">Free</span></div>
  </div>
  <div class="count"><span class="count__value">50</span><span class="count__label">Capsules</span></div>
</section>

</body>
</html>
```